Business Card and stationery
Use same font as used in my logo
Delia Frost
4127 E Copper Ln
Scottsdale, Az 85299
delia@thewillowparlorshop.com
www.thewillowparlorshop.com
Store Hours
Wed & Fri 11am - 3 pm
And By Appointment

```html
<!DOCTYPE html>
<html lang="en">
<head>
<meta charset="utf-8">
<title>Larkspur Boutique – Business Card</title>
<link href="https://fonts.googleapis.com/css2?family=Source+Sans+3:wght@400;600;700&display=swap" rel="stylesheet">
<style>
  :root {
    --backdrop: #b38f3c;
    --card-frame: #111111;
    --card-face: #ffffff;
    --card-shade: #ececec;
    --ink: #1a1a1a;
    --ink-soft: #333333;
  }
  * { margin: 0; padding: 0; box-sizing: border-box; }
  html, body { width: 1200px; height: 686px; overflow: hidden; }
  body {
    background: var(--backdrop);
    font-family: "Source Sans 3", Arial, sans-serif;
    color: var(--ink);
    position: relative;
  }
  .card {
    position: absolute;
    background: var(--card-frame);
    box-shadow: 0 3px 10px rgba(0,0,0,0.35);
  }
  .card-face {
    position: absolute;
    inset: 8px;
    border-radius: 22px;
    background: radial-gradient(ellipse at 50% 40%, var(--card-face) 55%, var(--card-shade) 100%);
    display: flex;
    flex-direction: column;
    align-items: center;
  }
  .card--front { left: 115px; top: 101px; width: 456px; height: 273px; }
  .card--back  { left: 672px; top: 238px; width: 422px; height: 254px; }

  .brand-box {
    margin-top: 22px;
    width: 198px;
    height: 90px;
    border: 2px solid var(--ink);
    padding: 4px;
  }
  .brand-box-inner {
    width: 100%; height: 100%;
    border: 1px dashed var(--ink);
    display: flex; align-items: center; justify-content: center; gap: 8px;
  }
  .brand-name {
    font-weight: 700;
    font-size: 22px;
    color: var(--ink);
    line-height: 1;
  }
  .brand-mark {
    width: 12px; height: 12px; border-radius: 50%;
    background: var(--ink);
  }
  .holder-name {
    margin-top: 48px;
    font-weight: 700;
    font-size: 18px;
  }
  .address { margin-top: 4px; font-size: 13px; color: var(--ink-soft); }
  .contact-row {
    display: flex; align-items: center; gap: 18px;
    font-size: 13px; color: var(--ink-soft); margin-top: 4px;
  }
  .contact-row--wide { width: 408px; justify-content: space-between; }
  .contact-item { display: flex; align-items: center; gap: 5px; }
  .contact-item svg { width: 13px; height: 13px; fill: var(--ink); }

  .card--back .brand-lockup {
    margin-top: 76px;
    display: flex; align-items: center; gap: 10px;
  }
  .card--back .brand-name { font-size: 30px; }
  .card--back .brand-mark { width: 16px; height: 16px; }
  .hours-title { margin-top: 30px; font-weight: 700; font-size: 18px; }
  .hours-line { font-size: 14px; color: var(--ink-soft); line-height: 1.25; }
</style>
</head>
<body>

<section class="card card--front" aria-label="Business card front">
  <div class="card-face">
    <div class="brand-box">
      <div class="brand-box-inner">
        <span class="brand-mark"></span>
        <span class="brand-name">Larkspur Boutique</span>
      </div>
    </div>
    <p class="holder-name">Delia Frost</p>
    <p class="address">4127 E Copper Ln Scottsdale, Az 85299</p>
    <div class="contact-row">
      <span class="contact-item">
        <svg viewBox="0 0 16 16"><path d="M3.6 1.2l2.3 2.6-1.3 1.6c.9 2 2.4 3.5 4.4 4.4l1.6-1.3 2.6 2.3-1.4 2.2C7 14.4 1.6 9 1.4 2.6z"/></svg>
        480-555-0147
      </span>
      <span class="contact-item">
        <svg viewBox="0 0 16 16"><rect x="4" y="1" width="8" height="4"/><rect x="1" y="6" width="14" height="6" rx="1"/><rect x="4" y="10" width="8" height="5" fill="#fff" stroke="#111" stroke-width="1"/></svg>
        480-555-0192
      </span>
    </div>
    <div class="contact-row contact-row--wide">
      <span class="contact-item">
        <svg viewBox="0 0 16 16"><rect x="1" y="3" width="14" height="10" rx="1"/><path d="M1.5 3.5L8 9l6.5-5.5" stroke="#fff" stroke-width="1.2" fill="none"/></svg>
        delia@thewillowparlorshop.com
      </span>
      <span class="contact-item">
        <svg viewBox="0 0 16 16"><circle cx="8" cy="8" r="7"/><path d="M1 8h14M8 1c-3 3-3 11 0 14M8 1c3 3 3 11 0 14" stroke="#fff" stroke-width="1" fill="none"/></svg>
        www.thewillowparlorshop.com
      </span>
    </div>
  </div>
</section>

<section class="card card--back" aria-label="Business card back">
  <div class="card-face">
    <div class="brand-lockup">
      <span class="brand-mark"></span>
      <span class="brand-name">Larkspur Boutique</span>
    </div>
    <p class="hours-title">Store Hours</p>
    <p class="hours-line">Wed &amp; Fri 11am - 3 pm</p>
    <p class="hours-line">And By Appointment</p>
  </div>
</section>

</body>
</html>
```